Pine Ridge Traders, LLC- Global Beverage Company with 100% Cold Chain Logistics

Hey All, My Name is Dale, I am a young business owner in a competitive export space, but my niche is that I am shipping all of my beer around the world, "100% Cold Chain". This model is more costly, but it protects the integrity of the beer itself and will give folks in foreign countries the best representation of what US Craft Beer has to offer.

I am not a branding guy and don't claim to be one, I am a salesperson first, and will be referring to all of you to create something great that will be memorable.

I am looking for a basic Business Card Design for my Craft Beer Export company. I sell US Craft Beer in several countries around the globe. Austrailia, China, Taiwan, Chile, France, New Zealand... to name a few.

I am looking for a sleek, modern, and fresh design. Quickly!

Thanks for your consideration!

Cheers,

Dale

Target Market(s)

International

Contact Information for Business Card

Dale Corwin
Founder- Roving Hops Guy
Dale@PineRidgeTraders.example
@RovingHopsGuy- Instagram only
www.Pineridgetraders.example
@PineRidgeTradersAU- Instagram Only

Font styles to use
Serif

Colors
0592cd
ffffff

Requirements
Must have
• Name-
• Title-
• Email-
• Social Media Handle-
• Company Website-
Nice to have
• Nice Logo/ Images on Card
Should not have
• Tacky Beer Images

```html
<!DOCTYPE html>
<html lang="en">
<head>
<meta charset="utf-8">
<title>Pine Ridge Traders — Business Card</title>
<link rel="stylesheet" href="https://fonts.googleapis.com/css2?family=Questrial&display=swap">
<style>
  :root {
    --brand-blue: #0592cd;
    --brand-blue-text: #1578b8;
    --brand-blue-deep: #0b4a6e;
    --brand-blue-mid: #0a79ad;
    --card-white: #ffffff;
    --paper-shade: #f1f3f5;
    --stage: #e4e7ea;
    --muted-text: #3d5a70;
    --divider: #8fc6e4;
  }
  * { box-sizing: border-box; margin: 0; padding: 0; }
  html, body {
    width: 1200px;
    height: 675px;
    overflow: hidden;
  }
  body {
    background: var(--stage);
    font-family: "Questrial", sans-serif;
    position: relative;
  }
  .card {
    position: absolute;
    top: 189px;
    width: 520px;
    height: 297px;
    border-radius: 3px;
    box-shadow: 0 10px 26px rgba(20, 40, 60, 0.18);
    overflow: hidden;
  }
  /* Front side */
  .card--front {
    left: 50px;
    background: linear-gradient(180deg, var(--card-white) 0%, var(--paper-shade) 100%);
  }
  .brand-mark {
    position: absolute;
    top: 30px;
    left: 30px;
    display: flex;
    align-items: center;
    gap: 8px;
  }
  .brand-mark__name {
    color: var(--brand-blue-text);
    font-size: 17px;
    line-height: 16px;
    letter-spacing: -0.2px;
  }
  .brand-mark__dot {
    width: 28px;
    height: 28px;
    border: 2px solid var(--brand-blue-text);
    border-radius: 50%;
  }
  .identity {
    position: absolute;
    top: 156px;
    right: 268px;
    text-align: right;
  }
  .identity__name {
    color: var(--brand-blue-text);
    font-size: 22px;
    letter-spacing: 0.2px;
  }
  .identity__title {
    color: var(--muted-text);
    font-size: 8.5px;
    margin-top: 3px;
  }
  .divider {
    position: absolute;
    left: 262px;
    top: 118px;
    width: 1px;
    height: 106px;
    background: var(--divider);
  }
  .contact {
    position: absolute;
    left: 278px;
    top: 124px;
    list-style: none;
    color: var(--muted-text);
    font-size: 10.5px;
    line-height: 25px;
  }
  /* Back side */
  .card--back {
    left: 630px;
    background: radial-gradient(ellipse at 50% 42%, var(--brand-blue) 0%, var(--brand-blue-mid) 45%, var(--brand-blue-deep) 100%);
    display: flex;
    align-items: center;
    justify-content: center;
  }
  .brand-lockup {
    display: flex;
    align-items: center;
    gap: 14px;
  }
  .brand-lockup__name {
    color: var(--card-white);
    font-size: 34px;
    line-height: 31px;
  }
  .brand-lockup__ring {
    width: 70px;
    height: 70px;
    border: 3px solid var(--card-white);
    border-radius: 50%;
  }
</style>
</head>
<body>
  <section class="card card--front" aria-label="Card front">
    <div class="brand-mark">
      <div class="brand-mark__name">Pine<br>Ridge<br>Traders</div>
      <div class="brand-mark__dot"></div>
    </div>
    <div class="identity">
      <h1 class="identity__name">Dale Corwin</h1>
      <p class="identity__title">Founder - Roving Hops Guy</p>
    </div>
    <div class="divider"></div>
    <ul class="contact">
      <li>Dale@PineRidgeTraders.example</li>
      <li>@RovingHopsGuy</li>
      <li>www.Pineridgetraders.example</li>
    </ul>
  </section>

  <section class="card card--back" aria-label="Card back">
    <div class="brand-lockup">
      <div class="brand-lockup__name">Pine<br>Ridge<br>Traders</div>
      <div class="brand-lockup__ring"></div>
    </div>
  </section>
</body>
</html>
```